Kivo Commercial Cleaning is lookong for a new business card design.

A fresh new design that's professional and stylish. We need a serious upgrade to our business cards. I have included pictures of our existing ones. Our clients include professional individuals and business owners. We woupdblike something professional and upbeat. Please have fun and see what you come uo with.

Target Market(s)

Property managers, business owners, facility managers and other similar professionals

Industry/Entity Type

Janitorial

Contact Information for Business Card

Name, cell, office number, email, web address

Font styles to use
Sans Serif

Colors

Designer to choose colors to be used in the design.

Requirements
Must have
• please use the green color in our logo
Nice to have
• Bar code
Should not have
• Address

```html
<!DOCTYPE html>
<html lang="en">
<head>
<meta charset="utf-8">
<title>Kivo Commercial Cleaning — Business Card</title>
<link href="https://fonts.googleapis.com/css2?family=Montserrat:wght@400;500;700&display=swap" rel="stylesheet">
<style>
  :root {
    --page-bg: #e4e4e3;
    --brand-blue: #2f6498;
    --brand-blue-light: #4479ab;
    --brand-green: #2ea84a;
    --card-white: #efefef;
    --text-grey: #555a60;
    --white: #f3f2f0;
  }
  * { margin: 0; padding: 0; box-sizing: border-box; }
  html, body {
    width: 1200px; height: 1200px; overflow: hidden;
    background: var(--page-bg);
    font-family: "Montserrat", Arial, sans-serif;
  }
  .card {
    position: absolute; left: 234px; width: 731px; height: 418px;
  }
  .card-front {
    top: 160px;
    background: linear-gradient(120deg, var(--brand-blue) 0%, var(--brand-blue-light) 100%);
    color: var(--white);
    text-align: center;
  }
  .front-wordmark {
    position: absolute; left: 0; right: 0; top: 112px;
    font-size: 118px; font-weight: 700; letter-spacing: 2px; line-height: 1;
  }
  .front-descriptor {
    position: absolute; left: 0; right: 0; top: 266px;
    font-size: 21px; font-weight: 500; letter-spacing: 0.5px;
  }
  .front-tagline {
    position: absolute; left: 0; right: 0; top: 364px;
    font-size: 17px; font-weight: 400; letter-spacing: 0.8px;
  }
  .card-back {
    top: 632px;
    background: linear-gradient(120deg, #e6e6e6 0%, var(--card-white) 60%, #f4f4f4 100%);
  }
  .person-name {
    position: absolute; left: 58px; top: 52px;
    font-size: 29px; font-weight: 700; color: var(--brand-blue);
  }
  .company-name {
    position: absolute; left: 58px; top: 252px;
    font-size: 18.5px; font-weight: 700; color: var(--brand-green);
  }
  .contact-list {
    position: absolute; left: 58px; top: 283px; list-style: none;
  }
  .contact-item {
    display: flex; align-items: center; height: 28px;
    font-size: 18.5px; color: var(--text-grey);
  }
  .contact-icon { width: 16px; height: 16px; margin-right: 10px; fill: var(--brand-blue); }
  .back-wordmark {
    position: absolute; right: 58px; top: 172px;
    font-size: 86px; font-weight: 700; line-height: 1; color: var(--brand-green);
  }
</style>
</head>
<body>
  <section class="card card-front">
    <div class="front-wordmark">kivo</div>
    <div class="front-descriptor">kivo commercial cleaning</div>
    <div class="front-tagline">better because we care</div>
  </section>

  <section class="card card-back">
    <h1 class="person-name">Dana Whitfield</h1>
    <div class="company-name">Kivo Commercial Cleaning</div>
    <ul class="contact-list">
      <li class="contact-item">
        <svg class="contact-icon" viewBox="0 0 24 24" aria-hidden="true"><path d="M6.6 10.8a15.1 15.1 0 0 0 6.6 6.6l2.2-2.2a1 1 0 0 1 1-.25 11.4 11.4 0 0 0 3.6.57 1 1 0 0 1 1 1V20a1 1 0 0 1-1 1A17 17 0 0 1 3 4a1 1 0 0 1 1-1h3.5a1 1 0 0 1 1 1c0 1.25.2 2.45.57 3.57a1 1 0 0 1-.25 1z"/></svg>
        (555) 014-2739
      </li>
      <li class="contact-item">
        <svg class="contact-icon" viewBox="0 0 24 24" aria-hidden="true"><path d="M2 5h20v14H2z M2 5l10 7 10-7" fill="none" stroke="#2f6498" stroke-width="0"/><path d="M2 5h20v2l-10 6L2 7z"/><path d="M2 9l10 6 10-6v10H2z"/></svg>
        dana@kivocleaning.com
      </li>
      <li class="contact-item">
        <svg class="contact-icon" viewBox="0 0 24 24" aria-hidden="true"><circle cx="12" cy="12" r="10"/><path d="M12 2v20M2 12h20M12 2c-4 4-4 16 0 20M12 2c4 4 4 16 0 20" fill="none" stroke="#efefef" stroke-width="1.6"/></svg>
        www.kivocleaning.com
      </li>
    </ul>
    <div class="back-wordmark">kivo</div>
  </section>
</body>
</html>
```